Easter & Summer School Dance Camps

I need two flyers one for Easter camps and one for summer school
We are a performing arts and dance academy

I want a double sided flyers one side summer school one side easter camp

Please make these flyers appeal to young dancers and performers - eye catching up to date Added Tuesday, March 1, 2016

Target Market(s)

Young children and teenagers

Industry/Entity Type

School

Font styles to use
Serif
Sans Serif

Requirements
Must have
• bright colourful

```html
<!DOCTYPE html>
<html lang="en">
<head>
<meta charset="utf-8">
<title>Once Upon a Time – Easter Workshops</title>
<link rel="stylesheet" href="https://fonts.googleapis.com/css2?family=Bitter:wght@700;800&family=Libre+Baskerville:ital,wght@0,400;0,700;1,400&family=Cormorant+Garamond:wght@500&display=swap">
<style>
  :root {
    --blue: #1576bd;
    --pink: #d6418f;
    --ink: #1a1a1a;
    --paper: #ffffff;
  }
  * { margin: 0; padding: 0; box-sizing: border-box; }
  html, body { width: 847px; height: 1200px; overflow: hidden; background: var(--paper); }
  .flyer { position: relative; width: 847px; height: 1200px; overflow: hidden; background: var(--paper); color: var(--ink); font-family: "Libre Baskerville", Georgia, serif; }
  .decor { position: absolute; inset: 0; width: 847px; height: 1200px; }
  .brand { position: absolute; left: 152px; top: 58px; display: flex; align-items: center; gap: 8px; }
  .brand-dot { width: 14px; height: 14px; border-radius: 50%; background: var(--pink); }
  .brand-name { font-family: "Libre Baskerville", Georgia, serif; font-weight: 400; font-size: 28px; color: var(--ink); }
  .title-word { position: absolute; font-family: "Bitter", Georgia, serif; font-weight: 800; color: var(--blue); font-size: 100px; line-height: 1; white-space: nowrap; }
  .title-once { left: 143px; top: 162px; }
  .title-upon { left: 407px; top: 162px; }
  .title-time { left: 470px; top: 246px; font-size: 96px; }
  .subtitle { position: absolute; font-family: "Cormorant Garamond", Georgia, serif; font-weight: 500; font-size: 40px; letter-spacing: 9px; line-height: 1; color: var(--ink); }
  .sub-west { left: 170px; top: 258px; }
  .sub-end { left: 213px; top: 298px; }
  .sub-workshop { left: 214px; top: 338px; }
  .content { position: absolute; left: 180px; width: 640px; text-align: center; font-size: 16px; line-height: 24px; white-space: nowrap; }
  .content p + p { margin-top: 24px; }
  .heading { font-weight: 700; font-size: 16px; }
  .intro { top: 421px; }
  .session-teens { top: 959px; }
  .session-teens p + p { margin-top: 0; }
  .slogan { position: absolute; left: 180px; top: 802px; width: 640px; text-align: center; font-weight: 700; font-size: 21px; line-height: 33.5px; letter-spacing: 0.5px; white-space: nowrap; }
  .contact { position: absolute; left: 150px; top: 1103px; width: 700px; text-align: center; font-family: "Cormorant Garamond", Georgia, serif; font-weight: 500; font-size: 21px; line-height: 24px; letter-spacing: 0.5px; white-space: nowrap; }
</style>
</head>
<body>
<div class="flyer">
  <svg class="decor" viewBox="0 0 847 1200" aria-hidden="true">
    <defs>
      <radialGradient id="sphere" cx="0.55" cy="0.3" r="0.8">
        <stop offset="0" stop-color="#f8dcea"/>
        <stop offset="0.45" stop-color="#eb92bf"/>
        <stop offset="1" stop-color="#d2338a"/>
      </radialGradient>
      <linearGradient id="blue-star" x1="0" y1="0" x2="1" y2="1">
        <stop offset="0" stop-color="#19a6e0"/>
        <stop offset="1" stop-color="#0f6cb8"/>
      </linearGradient>
      <linearGradient id="pink-star" x1="0" y1="0" x2="1" y2="1">
        <stop offset="0" stop-color="#f39ac6"/>
        <stop offset="0.5" stop-color="#df4b9a"/>
        <stop offset="1" stop-color="#b8237a"/>
      </linearGradient>
      <linearGradient id="rule" x1="0" y1="0" x2="1" y2="0">
        <stop offset="0" stop-color="#d94c97"/>
        <stop offset="1" stop-color="#e06aa8"/>
      </linearGradient>
      <polygon id="star" points="0,-1 0.24,-0.33 0.95,-0.31 0.39,0.13 0.59,0.81 0,0.42 -0.59,0.81 -0.39,0.13 -0.95,-0.31 -0.24,-0.33"/>
    </defs>
    <g class="spheres">
      <circle cx="-32" cy="76" r="76" fill="url(#sphere)"/>
      <circle cx="-2" cy="356" r="146" fill="url(#sphere)"/>
      <circle cx="42" cy="752" r="212" fill="url(#sphere)"/>
      <circle cx="94" cy="1140" r="128" fill="url(#sphere)"/>
    </g>
    <g class="blue-stars" fill="url(#blue-star)">
      <use href="#star" transform="translate(705 -25) rotate(15) scale(90)"/>
      <use href="#star" transform="translate(880 105) rotate(-10) scale(55)"/>
      <use href="#star" transform="translate(880 385) rotate(-20) scale(90)"/>
      <use href="#star" transform="translate(885 735) rotate(-15) scale(130)"/>
      <use href="#star" transform="translate(880 1070) rotate(-20) scale(80)"/>
    </g>
    <use href="#star" fill="url(#pink-star)" transform="translate(394 284) rotate(-8) scale(66)"/>
    <polygon class="rule" points="296,776 696,780 296,788" fill="url(#rule)"/>
    <polygon class="rule" points="296,930 696,925 696,937" fill="url(#rule)"/>
  </svg>

  <div class="brand">
    <span class="brand-dot"></span>
    <span class="brand-name">Moonbeam Academy</span>
  </div>

  <h1>
    <span class="title-word title-once">Once</span>
    <span class="title-word title-upon">Upon</span>
    <span class="title-word title-time">a Time</span>
  </h1>
  <div class="subtitle sub-west">WEST</div>
  <div class="subtitle sub-end">END</div>
  <div class="subtitle sub-workshop">WORKSHOP</div>

  <div class="content intro">
    <p class="heading">EASTER WORKSHOPS</p>
    <p>This spring, your child will enjoy a joyous journey to the magical<br>world of <em>Once Upon a Time</em> for a fabulous springtime treat.</p>
    <p>We will work our magic to ensure your child enjoys every minute.<br>Guiding each child every step of the way and inspire and<br>encourage them to project their voices, learn energetic dance<br>routines, sing catchy songs, and more importantly HAVE FUN!</p>
    <p class="session session-kids"><strong>Tuesday, 5 &amp; 6 April 2016</strong><br>Age 3 – 7 years<br>10 – 12 p.m.<br>18/day or 30/both days</p>
  </div>

  <p class="slogan">Our Easter dance camps are fun,<br>fresh and funky, mixed together<br>with a little musical theatre!</p>

  <div class="content session session-teens">
    <p class="heading">WEST END WORKSHOP</p>
    <p><strong>Tuesday, 5 &amp; 6 April 2016</strong></p>
    <p>8 – 16 years</p>
    <p>1 – 4 p.m.</p>
    <p>30 /day or 55/both days</p>
  </div>

  <div class="contact">
    <p>Venue: The Church Hall of St Anne Millbrook KT9 4ZZ</p>
    <p>Email: moonbeamdancebiz@gmail to book or text 07700900461</p>
  </div>
</div>
</body>
</html>
```